Graphic Design for Application Form and Menu

We are a success education company called Tandem Crestline. We are designing a USB application for a personal development program that will be cross platform (PC/Mac). The product is called Quiet Harvest, Meridale Academy (These logos are already created). The program will open pdf books in a Flash reader, play audio and video files in the default media player, and open windows for recording entries in a journal and for setting goals.
We need a graphic design for a small control panel (300px X 300px) to launch the different modules of the program.

We are looking for a design that is clean and professional.
A sample is included of everything that needs to be on the form. A sample menu is also included. We are looking for other designs for the form and menu.
Updates

Industry/Entity Type

Graphic Design

Requirements
Must have
• The panel will have: a menu, two toolbars, and two status panels.
ItemDetails:
A menu will have items for "Welcome, Profile, and Kudos."
One tool bar will have items for "Guidebooks (w/9 item popup menu), Audios (w/9 item popup menu), Videos (w/9 item popup menu), Journal (w/2 item popup menu), and Goals."
A second tool bar will have items for "Blog, Community, Events, Sovereignty, Foundation, and Influence."
The tool bars should have icons and text.
There should be two status panel, one for Audio and one for Video.
The status panels should show the name of the audio or video that is opened, have check boxes for: Add to favorites, Come back, and Done, and have links for: Audios, Top Posts, Post, and Tips.

```html
<!DOCTYPE html>
<html lang="en">
<head>
<meta charset="utf-8">
<title>Control Panel</title>
<link href="https://fonts.googleapis.com/css2?family=Arimo:wght@400;700&display=swap" rel="stylesheet">
<style>
  :root {
    --page: #ffffff;
    --accent: #1fb0e6;
    --accent-strong: #00b9f0;
    --frame: #2aa9dc;
    --bar-top: #ffffff;
    --bar-bottom: #dcdcdc;
    --label: #4a4a4a;
    --status-bg: #d5d5d5;
    --pill-border: #8fd3ee;
    --pill-text: #c4c4c4;
    --close: #f3b5b5;
    --close-edge: #d98787;
  }
  * { box-sizing: border-box; margin: 0; padding: 0; }
  html, body { width: 1200px; height: 1200px; overflow: hidden; background: var(--page); }
  body { position: relative; font-family: "Arimo", Arial, sans-serif; }

  .panel {
    position: absolute; left: 28px; top: 28px; width: 1140px; height: 1148px;
    border: 3px solid var(--frame); border-radius: 40px; background: #fff;
    box-shadow: 6px 8px 12px rgba(0,0,0,0.35);
  }
  .close {
    position: absolute; left: 1110px; top: 24px; width: 40px; height: 40px; border-radius: 50%;
    background: radial-gradient(circle at 40% 35%, #fde3e3, var(--close));
    border: 2px solid var(--close-edge);
  }
  .close svg { position: absolute; left: 9px; top: 9px; }

  .main-menu { position: absolute; left: 78px; top: 44px; display: flex; gap: 56px; }
  .main-menu span { color: var(--accent); font-size: 48px; }

  .toolbar {
    position: absolute; left: 56px; width: 1072px; height: 160px;
    border: 3px solid var(--frame); border-radius: 60px;
    background: linear-gradient(var(--bar-top) 35%, var(--bar-bottom));
    display: flex;
  }
  .toolbar.modules { top: 136px; }
  .toolbar.community { top: 974px; height: 162px; }
  .tool { position: relative; height: 100%; text-align: center; color: var(--label); font-size: 26px; }
  .modules .tool + .tool { border-left: 2px solid var(--frame); }
  .tool svg { position: absolute; left: 50%; top: 22px; transform: translateX(-50%); }
  .tool .label { position: absolute; left: 0; right: 0; top: 104px; letter-spacing: 1px; }
  .community .tool .label { top: 112px; letter-spacing: 0.5px; }
  .swatch { position: absolute; left: 50%; top: 26px; width: 74px; height: 74px; transform: translateX(-50%); border-radius: 8px; }

  .status-title { position: absolute; top: 320px; width: 300px; text-align: center; color: var(--accent); font-size: 38px; }
  .status {
    position: absolute; top: 392px; width: 456px; height: 532px;
    background: var(--status-bg); border-radius: 24px;
    box-shadow: 4px 6px 10px rgba(0,0,0,0.35);
  }
  .now-playing {
    position: absolute; left: 20px; top: 32px; width: 410px; height: 76px;
    background: var(--accent-strong); border-radius: 24px;
  }
  .pill {
    position: absolute; left: 20px; width: 406px; height: 60px;
    border: 2px solid var(--pill-border); border-radius: 30px;
    background: linear-gradient(#ffffff 50%, #ececec);
    color: var(--pill-text); font-size: 36px; text-align: center; line-height: 56px;
  }
  .pill.come-back { top: 134px; }
  .pill.favorites { top: 200px; }
  .pill.done { top: 264px; }
  .link { position: absolute; color: var(--accent); font-size: 31px; text-decoration: underline; }
  .link.audios { left: 36px; top: 364px; }
  .link.post { right: 42px; top: 362px; }
  .link.top-posts { left: 36px; top: 444px; }
  .link.tips { right: 42px; top: 442px; }
</style>
</head>
<body>
<div class="panel"></div>
<div class="close">
  <svg width="18" height="18" viewBox="0 0 18 18"><path d="M2 2 L16 16 M16 2 L2 16" stroke="#b85f5f" stroke-width="3"/></svg>
</div>

<nav class="main-menu"><span>Welcome</span><span>Profile</span><span>Kudos</span></nav>

<div class="toolbar modules">
  <div class="tool" style="width:256px">
    <svg width="84" height="72" viewBox="0 0 84 72"><path d="M42 18 Q26 6 6 12 L10 60 Q28 54 42 64 Q56 54 74 60 L78 12 Q58 6 42 18 Z M42 18 L42 64" fill="#fff" stroke="#222" stroke-width="3"/></svg>
    <div class="label">GuideBook</div>
  </div>
  <div class="tool" style="width:190px">
    <svg width="84" height="72" viewBox="0 0 84 72"><path d="M6 26 H22 L42 10 V62 L22 46 H6 Z" fill="#111"/><path d="M52 24 Q60 36 52 48 M60 16 Q74 36 60 56 M68 8 Q88 36 68 64" fill="none" stroke="#111" stroke-width="3"/></svg>
    <div class="label">Audios</div>
  </div>
  <div class="tool" style="width:200px">
    <svg width="96" height="72" viewBox="0 0 96 72"><rect x="4" y="12" width="62" height="50" fill="#000"/><path d="M66 30 L92 14 V60 L66 44 Z" fill="#000"/></svg>
    <div class="label">Videos</div>
  </div>
  <div class="tool" style="width:182px">
    <svg width="84" height="84" viewBox="0 0 84 84"><rect x="4" y="4" width="76" height="76" rx="12" fill="#8a8a8a" stroke="#333" stroke-width="3"/><rect x="14" y="14" width="56" height="56" rx="8" fill="#e6e6e6"/><path d="M24 62 L30 46 L56 20 L64 28 L38 54 Z" fill="#555"/></svg>
    <div class="label">Journal</div>
  </div>
  <div class="tool" style="width:238px">
    <svg width="84" height="72" viewBox="0 0 84 72"><rect x="4" y="4" width="76" height="64" fill="#000"/><path d="M12 50 L30 30 L46 44 L70 16 M12 60 L32 40 L48 54 L72 28" fill="none" stroke="#fff" stroke-width="3"/></svg>
    <div class="label">Goals</div>
  </div>
</div>

<div class="status-title" style="left:164px">Audio</div>
<div class="status-title" style="left:722px">Video</div>

<section class="status" style="left:86px" aria-label="Audio status">
  <div class="now-playing"></div>
  <div class="pill come-back">Come Back</div>
  <div class="pill favorites">Add to Favorites</div>
  <div class="pill done">Done</div>
  <span class="link audios">Audios</span><span class="link post">Post</span>
  <span class="link top-posts">Top Posts</span><span class="link tips">Tips</span>
</section>

<section class="status" style="left:644px" aria-label="Video status">
  <div class="now-playing"></div>
  <div class="pill come-back">Come Back</div>
  <div class="pill favorites">Add to Favorites</div>
  <div class="pill done">Done</div>
  <span class="link audios">Audios</span><span class="link post">Post</span>
  <span class="link top-posts">Top Posts</span><span class="link tips">Tips</span>
</section>

<div class="toolbar community">
  <div class="tool" style="width:130px;margin-left:10px">
    <div class="swatch" role="img" aria-label="Blog icon" style="background:linear-gradient(#f6a36a,#e0642b)"></div>
    <div class="label">Blog</div>
  </div>
  <div class="tool" style="width:160px">
    <div class="swatch" role="img" aria-label="Community icon" style="background:linear-gradient(#bff0fa,#7fd8ee)"></div>
    <div class="label">Community</div>
  </div>
  <div class="tool" style="width:136px">
    <div class="swatch" role="img" aria-label="Events icon" style="background:linear-gradient(#f7d774,#d38a1d)"></div>
    <div class="label">Events</div>
  </div>
  <div class="tool" style="width:192px">
    <div class="swatch" role="img" aria-label="Sovereignty icon" style="background:linear-gradient(#a86fe0,#5b2596)"></div>
    <div class="label">Sovereignty</div>
  </div>
  <div class="tool" style="width:196px">
    <div class="swatch" role="img" aria-label="Foundation icon" style="background:linear-gradient(#d86a3c,#7a2414)"></div>
    <div class="label">Foundation</div>
  </div>
  <div class="tool" style="width:176px">
    <div class="swatch" role="img" aria-label="Influence icon" style="background:linear-gradient(#3a3a3a,#000)"></div>
    <div class="label">Influence</div>
  </div>
</div>
</body>
</html>
```